Business Card Design Project

We are a distribution company providing goods to Latin America. We sell everything from Medical equipment, generic medicines, to carecliners. The logo that we use is attached. The logo can incorporate different colors other than black for versatility. The company name is Valdoria International Corporation and/or VIC. The card will be printed using 1 or more of the following: Silk mounted and/or embossed. So if the design ideas could be made to incorporate that technique or any other unique techniques, it would be great. The target market is dialysis centers/doctors.

Basic Info for card:
Marnie Dowsett
Purchasing Manager
555-317-4086 direct
555-241-7953 fax
marnie.dowsett@valdoriavic.example
www.valdoriavic.example

Target Market(s)

Latin America

Industry/Entity Type

Business

Requirements
Nice to have
• The Front of the card should have the basic contact information with company name/logo. The back of the card could incorporate

```html
<!DOCTYPE html>
<html lang="en">
<head>
<meta charset="utf-8">
<title>Valdoria International Corporation – Business Card</title>
<link rel="stylesheet" href="https://fonts.googleapis.com/css2?family=Cinzel:wght@400;600&family=Cormorant+Garamond:wght@500&display=swap">
<style>
  :root {
    --backdrop: #ecebe9;
    --card-top: #3a3939;
    --card-bottom: #1c1c1c;
    --silver: #d9d9d9;
    --silver-dim: #b9b9b9;
    --rule-dark: #121212;
    --rule-light: #4a4a4a;
    --brand-red: #8e1b17;
  }
  html, body {
    margin: 0;
    width: 1200px;
    height: 599px;
    overflow: hidden;
    background: var(--backdrop);
  }
  .stage {
    width: 1200px;
    height: 599px;
    display: flex;
    align-items: center;
    justify-content: center;
  }
  .card {
    position: relative;
    width: 840px;
    height: 480px;
    background: linear-gradient(160deg, var(--card-top) 0%, #2a2a2a 45%, var(--card-bottom) 100%);
    box-shadow: 0 12px 30px rgba(0,0,0,0.25);
    color: var(--silver);
    overflow: hidden;
  }
  .rule {
    position: absolute;
    left: 0;
    right: 0;
    height: 0;
    border-top: 1px solid var(--rule-dark);
    border-bottom: 1px solid var(--rule-light);
  }
  .rule--upper { top: 158px; }
  .rule--lower { top: 300px; }
  .brand {
    position: absolute;
    left: 56px;
    top: 188px;
    display: flex;
    align-items: center;
    gap: 14px;
    font-family: "Cinzel", serif;
    font-weight: 600;
    font-size: 54px;
    letter-spacing: 6px;
    color: var(--brand-red);
  }
  .brand__mark {
    width: 22px;
    height: 22px;
    background: var(--brand-red);
  }
  .identity {
    position: absolute;
    right: 56px;
    top: 74px;
    text-align: right;
    font-family: "Cinzel", serif;
  }
  .identity__name {
    margin: 0;
    font-size: 38px;
    font-weight: 600;
    letter-spacing: 1px;
    line-height: 1;
  }
  .identity__title {
    margin: 4px 0 0;
    font-size: 15px;
    letter-spacing: 1.5px;
    color: var(--silver-dim);
  }
  .online {
    position: absolute;
    right: 56px;
    top: 196px;
    text-align: right;
    font-family: "Cormorant Garamond", serif;
    font-weight: 500;
    font-size: 24px;
    line-height: 32px;
  }
  .address {
    position: absolute;
    left: 56px;
    top: 326px;
    font-family: "Cinzel", serif;
    font-size: 24px;
    letter-spacing: 5px;
  }
  .phones {
    position: absolute;
    left: 56px;
    top: 384px;
    font-family: "Cormorant Garamond", serif;
    font-weight: 500;
    font-size: 26px;
    line-height: 32px;
  }
  .online p, .phones p { margin: 0; }
</style>
</head>
<body>
  <main class="stage">
    <article class="card" aria-label="Business card, front">
      <div class="rule rule--upper"></div>
      <div class="rule rule--lower"></div>

      <div class="brand">
        <span class="brand__mark" aria-hidden="true"></span>
        <span class="brand__name">VIC</span>
      </div>

      <header class="identity">
        <h1 class="identity__name">Marnie Dowsett</h1>
        <p class="identity__title">Purchasing Manager</p>
      </header>

      <div class="online">
        <p>marnie.dowsett@valdoriavic.example</p>
        <p>www.valdoriavic.example</p>
      </div>

      <p class="address">1478 SW 12th Avenue Miami, FL 33129</p>

      <div class="phones">
        <p>Phone 555.317.4086</p>
        <p>Fax 555.241.7953</p>
      </div>
    </article>
  </main>
</body>
</html>
```